Designs for a Barrister's chambers

Design stationery (including business card and letterhead) for a barrister's chambers -- similar to a law firm, using the enclosed logo. The current designs are not fit for purpose.

```html
<!DOCTYPE html>
<html lang="en">
<head>
<meta charset="utf-8">
<title>Ledgerhall Chambers Stationery</title>
<link href="https://fonts.googleapis.com/css2?family=Montserrat:wght@400;500;600;700&display=swap" rel="stylesheet">
<style>
  :root {
    --backdrop: #cfcfcf;
    --paper: #f4f4f4;
    --paper-shade: #e6e7e8;
    --navy: #1b2a47;
    --navy-deep: #121d33;
    --teal: #0a87a3;
    --teal-dark: #06708a;
    --teal-bright: #0fa0bd;
    --teal-pale: #a9d2dc;
    --ink: #1c2535;
  }
  * { box-sizing: border-box; margin: 0; padding: 0; }
  html, body { width: 1200px; height: 900px; overflow: hidden; }
  body {
    background: radial-gradient(ellipse at 50% 45%, #d6d6d6 0%, #c4c4c4 100%);
    font-family: "Montserrat", sans-serif;
    color: var(--ink);
    position: relative;
  }
  .sheet { position: absolute; overflow: hidden; box-shadow: 0 6px 18px rgba(0,0,0,0.18); }

  /* Letterhead */
  .letterhead {
    left: 115px; top: 47px; width: 407px; height: 575px;
    background: linear-gradient(160deg, var(--paper-shade) 0%, #f7f7f7 60%, #f1f1f1 100%);
  }
  .brand { position: absolute; display: flex; align-items: center; }
  .brand-mark {
    flex: none; border-radius: 50%;
    background: var(--teal);
  }
  .brand-name {
    font-weight: 600; color: var(--navy); line-height: 0.98; letter-spacing: -0.3px;
  }
  .letterhead .brand { left: 35px; top: 41px; gap: 10px; }
  .letterhead .brand-mark { width: 14px; height: 14px; }
  .letterhead .brand-name { font-size: 23px; }

  .contact-block {
    position: absolute; right: 28px; top: 38px;
    font-size: 5.6px; font-weight: 500; text-align: right; line-height: 1.15;
  }
  .contact-row { display: flex; justify-content: flex-end; align-items: center; gap: 5px; }
  .contact-row + .contact-row { margin-top: 3px; }
  .contact-row.spaced { margin-top: 8px; }
  .icon { width: 6px; height: 6px; fill: var(--teal); flex: none; }

  .watermark {
    position: absolute; left: 62px; top: 174px; width: 284px; height: 293px;
    background: radial-gradient(ellipse at 50% 50%, rgba(214,222,227,0.55) 0%, rgba(225,231,234,0.3) 45%, rgba(240,242,243,0) 72%);
  }
  .letter-footer {
    position: absolute; left: 0; right: 0; top: 506px;
    text-align: center; font-size: 5.6px; font-weight: 500; line-height: 10px;
  }
  .footer-rule { width: 110px; height: 1px; background: var(--teal); margin: 0 auto 9px; }
  .letter-band {
    position: absolute; left: 0; right: 0; bottom: 0; height: 15px;
    background: linear-gradient(90deg, var(--teal), var(--teal-bright));
  }

  /* Cover */
  .cover {
    left: 681px; top: 47px; width: 411px; height: 580px;
    background: linear-gradient(155deg, var(--navy-deep) 0%, var(--navy) 45%, var(--navy-deep) 100%);
  }
  .cover-pattern {
    position: absolute; inset: 0;
    background:
      radial-gradient(ellipse at 30% 35%, rgba(40,90,130,0.28), transparent 55%),
      radial-gradient(ellipse at 70% 70%, rgba(30,75,115,0.22), transparent 50%),
      linear-gradient(135deg, transparent 30%, rgba(60,110,150,0.08) 50%, transparent 70%);
  }
  .cover-emblem {
    position: absolute; right: 3px; bottom: 4px; width: 166px; height: 172px;
    background: radial-gradient(ellipse at 55% 55%, rgba(10,135,163,0.55) 0%, rgba(10,135,163,0.25) 50%, rgba(10,135,163,0) 78%);
  }

  /* Business card front */
  .card-front {
    left: 115px; top: 660px; width: 313px; height: 204px;
    background: linear-gradient(160deg, #ececec, #f6f6f6);
  }
  .card-front .brand { left: 16px; top: 17px; gap: 8px; }
  .card-front .brand-mark { width: 12px; height: 12px; }
  .card-front .brand-name { font-size: 21px; }
  .holder { position: absolute; left: 16px; top: 72px; }
  .holder-name { font-size: 14px; font-weight: 700; color: var(--teal); }
  .holder-role { font-size: 7.5px; font-weight: 500; margin-top: 1px; }
  .holder-address { font-size: 7.5px; line-height: 10px; margin-top: 8px; margin-left: 1px; }
  .holder-contacts { list-style: none; margin-top: 12px; font-size: 7.5px; line-height: 11.5px; }
  .holder-contacts li { display: flex; align-items: center; gap: 5px; }
  .holder-contacts .icon { width: 5.5px; height: 5.5px; fill: var(--navy); }
  .card-accent {
    position: absolute; right: 0; top: 56px; width: 97px; height: 148px;
    background: radial-gradient(ellipse at 80% 55%, rgba(169,210,220,0.85) 0%, rgba(169,210,220,0.4) 50%, rgba(169,210,220,0) 80%);
  }

  /* Business card back */
  .card-back {
    left: 472px; top: 660px; width: 310px; height: 202px;
    background: linear-gradient(150deg, var(--navy), var(--navy-deep));
  }
  .card-back-emblem {
    position: absolute; right: 0; bottom: 0; width: 113px; height: 117px;
    background: radial-gradient(ellipse at 60% 60%, rgba(10,135,163,0.6) 0%, rgba(10,135,163,0.25) 50%, rgba(10,135,163,0) 80%);
  }
</style>
</head>
<body>
  <svg width="0" height="0" style="position:absolute">
    <defs>
      <symbol id="i-pin" viewBox="0 0 10 10"><path d="M5 0a3.5 3.5 0 0 0-3.5 3.5C1.5 6 5 10 5 10s3.5-4 3.5-6.5A3.5 3.5 0 0 0 5 0zm0 5a1.5 1.5 0 1 1 0-3 1.5 1.5 0 0 1 0 3z"/></symbol>
      <symbol id="i-phone" viewBox="0 0 10 10"><path d="M0 3c0-1.5 2-3 5-3s5 1.5 5 3v1H7V2.5H3V4H0zM2 5h6l1 5H1z"/></symbol>
      <symbol id="i-fax" viewBox="0 0 10 10"><path d="M2 0h6v3H2zM0 4h10v6H0zm2 2v1h2V6zm4 0v1h2V6z"/></symbol>
      <symbol id="i-mobile" viewBox="0 0 10 10"><path d="M2.5 0h5v10h-5zm1 1v7h3V1z"/></symbol>
      <symbol id="i-mail" viewBox="0 0 10 10"><path d="M0 2h10v6H0zm1 1 4 3 4-3z"/></symbol>
      <symbol id="i-web" viewBox="0 0 10 10"><circle cx="5" cy="5" r="5"/></symbol>
    </defs>
  </svg>

  <section class="sheet letterhead" aria-label="Letterhead">
    <div class="brand">
      <span class="brand-mark"></span>
      <span class="brand-name">Ledgerhall<br>Chambers</span>
    </div>
    <div class="contact-block">
      <div class="contact-row"><span>82 Temple Row,<br>London EC4Y 7HN</span><svg class="icon"><use href="#i-pin"/></svg></div>
      <div class="contact-row spaced"><span>0203 555 0101</span><svg class="icon"><use href="#i-phone"/></svg></div>
      <div class="contact-row"><span>0203 555 0102</span><svg class="icon"><use href="#i-fax"/></svg></div>
      <div class="contact-row"><span>clerks@ledgerhallchambers.com</span><svg class="icon"><use href="#i-mail"/></svg></div>
      <div class="contact-row"><span>www.ledgerhallchambers.com</span><svg class="icon"><use href="#i-web"/></svg></div>
    </div>
    <div class="watermark" role="img" aria-label="Faint brand emblem watermark"></div>
    <div class="letter-footer">
      <div class="footer-rule"></div>
      <p>Ledgerhall Chambers Limited | Company Reg No: 10293847</p>
      <p>Registered Address: 9 Quayside Walk, London SE1 4QT</p>
      <p>VAT Registration No: 98765432</p>
    </div>
    <div class="letter-band"></div>
  </section>

  <section class="sheet cover" aria-label="Folder cover">
    <div class="cover-pattern" role="img" aria-label="Large faint emblem pattern"></div>
    <div class="cover-emblem" role="img" aria-label="Brand emblem in teal"></div>
  </section>

  <section class="sheet card-front" aria-label="Business card front">
    <div class="brand">
      <span class="brand-mark"></span>
      <span class="brand-name">Ledgerhall<br>Chambers</span>
    </div>
    <div class="holder">
      <p class="holder-name">Martin Ashcombe</p>
      <p class="holder-role">Barrister</p>
      <p class="holder-address">82 Temple Row,<br>London EC4Y 7HN</p>
      <ul class="holder-contacts">
        <li><svg class="icon"><use href="#i-phone"/></svg>0203 555 0101</li>
        <li><svg class="icon"><use href="#i-mobile"/></svg>07700 900 123</li>
        <li><svg class="icon"><use href="#i-fax"/></svg>0203 555 0102</li>
        <li><svg class="icon"><use href="#i-mail"/></svg>martin.ashcombe@ledgerhallchambers.com</li>
        <li><svg class="icon"><use href="#i-web"/></svg>www.ledgerhallchambers.com</li>
      </ul>
    </div>
    <div class="card-accent" role="img" aria-label="Pale brand emblem accent"></div>
  </section>

  <section class="sheet card-back" aria-label="Business card back">
    <div class="card-back-emblem" role="img" aria-label="Brand emblem in teal"></div>
  </section>
</body>
</html>
```